Looking for a creative label design for our retail coffee bags

We are a coffee manufacturer (coffee roaster) looking to re-brand our retail label for our coffee bags. Our main coffee blend that we sell is our Harborline Velvet Blend. You can use this name when creating the label. We are going for a look that represents our company as a coffee roaster. Please reference our website (www.brindlemugworks.com) and our Facebook page to learn more about our company and to give you more inspiration on creating this design.

Target Market(s)

Retail customers/grocery stores

Industry/Entity Type

Manufacturer

Requirements
Must have
• The size of the label has to be 3" width x 4" height

Logo must be Black
Nice to have
• We currently incorporate a color on our labels for each blend. For example, Harborline Velvet Blend (royal blue), Decaffeinated Blend (red), Breakfast Blend (green), Flavored coffees (gold).

Rustic/vintage style

```html
<!DOCTYPE html>
<html lang="en">
<head>
<meta charset="utf-8">
<title>Brindle Mugworks – Harborline Velvet Blend Label</title>
<link rel="stylesheet" href="https://fonts.googleapis.com/css2?family=Alfa+Slab+One&family=Yellowtail&family=Oswald:wght@500;700&display=swap">
<style>
  :root {
    --navy: #1b3557;
    --royal: #24507e;
    --teal: #3f8590;
    --sage: #93b59f;
    --amber: #c08a35;
    --umber: #6b4519;
    --ink: #111111;
    --paper: #f4efe3;
    --red: #b8141b;
    --gold: #c79a3c;
    --gold-light: #e2c074;
  }
  * { margin: 0; padding: 0; box-sizing: border-box; }
  html, body {
    width: 829px;
    height: 1200px;
    overflow: hidden;
    background: var(--paper);
  }
  .label {
    position: relative;
    width: 829px;
    height: 1200px;
    overflow: hidden;
    background:
      radial-gradient(ellipse at 50% 45%, rgba(255,255,255,0.18) 0%, rgba(255,255,255,0) 55%),
      radial-gradient(ellipse at 50% 50%, rgba(0,0,0,0) 55%, rgba(0,0,0,0.45) 100%),
      linear-gradient(180deg, var(--navy) 0%, var(--royal) 22%, var(--teal) 45%, var(--sage) 60%, var(--amber) 80%, var(--umber) 100%);
  }
  .brand {
    position: absolute;
    top: 70px;
    left: 50%;
    transform: translateX(-50%);
    width: 190px;
    height: 190px;
    border-radius: 50%;
    background: var(--ink);
    display: flex;
    align-items: center;
    justify-content: center;
    text-align: center;
  }
  .brand-name {
    font-family: "Oswald", sans-serif;
    font-weight: 700;
    font-size: 30px;
    line-height: 1.05;
    letter-spacing: 2px;
    color: var(--paper);
    text-transform: uppercase;
  }
  .tagline {
    position: absolute;
    top: 300px;
    width: 100%;
    text-align: center;
    font-family: "Yellowtail", cursive;
    font-size: 84px;
    color: var(--ink);
  }
  .blend-name {
    position: absolute;
    top: 420px;
    width: 100%;
    text-align: center;
    font-family: "Alfa Slab One", serif;
    font-size: 104px;
    line-height: 1;
    color: var(--red);
    letter-spacing: 1px;
  }
  .blend-sub {
    position: absolute;
    top: 538px;
    width: 100%;
    text-align: center;
    font-family: "Alfa Slab One", serif;
    font-size: 40px;
    color: var(--red);
    letter-spacing: 3px;
  }
  .seal {
    position: absolute;
    top: 700px;
    left: 50%;
    transform: translateX(-50%);
    width: 300px;
    height: 300px;
    border-radius: 50%;
    background: radial-gradient(circle at 45% 40%, var(--gold-light) 0%, var(--gold) 60%, #9a7226 100%);
    opacity: 0.85;
  }
</style>
</head>
<body>
  <main class="label">
    <div class="brand">
      <span class="brand-name">Brindle<br>Mugworks</span>
    </div>
    <p class="tagline">Fresh Roasted</p>
    <h1 class="blend-name">HARBORLINE</h1>
    <p class="blend-sub">VELVET BLEND</p>
    <div class="seal" role="img" aria-label="Gold anniversary seal for premium coffee"></div>
  </main>
</body>
</html>
```